The Linden Rooms. Psychotherapy practice. Looking for a multi-use design.

Hello, we need someone who can give us a design that's usable across business cards, rack cards and headed paper.
We're also looking for a logo that can be used on the cards and on the web site when we change the web site.
The current web site, www.the-linden-rooms.example.co.uk can be used to gather info, but does not need to be used for colour/design choices (e.g. one partner likes the Times font another prefers a sans-serif font. One likes the idea of a brass plaque in the design, the other doesn't).
The main point about the design is that it should convey an image of a professional service - their latest strap line is "Professional • Experienced • Confidential" used in a local ad.
Updates
The ladies have also asked me to add that although the Practice is very close to Marsh Priory, and one of the lines they use on the site is "Just a short walk from the Priory", they don't want it to look like something that's Christian or religious.
Thanks.

```html
<!DOCTYPE html>
<html lang="en">
<head>
<meta charset="utf-8">
<title>The Linden Rooms – Business Card</title>
<link rel="stylesheet" href="https://fonts.googleapis.com/css2?family=Open+Sans:wght@400;600;700&display=swap">
<style>
  :root {
    --page-bg: #e9e6e1;
    --navy-deep: #0d1330;
    --navy: #1f2f6e;
    --blue-glow: #5a7fd0;
    --brand-blue: #3a4f9c;
    --ink: #1d2233;
    --ink-soft: #3b4050;
    --white: #ffffff;
    --rule: #1d2233;
  }
  * { box-sizing: border-box; margin: 0; padding: 0; }
  html, body {
    width: 1200px; height: 784px; overflow: hidden;
    background: var(--page-bg);
    font-family: "Open Sans", Arial, sans-serif;
  }
  .sheet {
    width: 1200px; height: 784px;
    display: flex; align-items: center; justify-content: center; gap: 40px;
  }
  .card {
    position: relative;
    width: 540px; height: 310px;
    overflow: hidden;
    box-shadow: 0 6px 18px rgba(0,0,0,0.18);
  }

  /* Front */
  .card--front { color: var(--white); }
  .front-scene {
    position: absolute; inset: 0;
    background:
      radial-gradient(ellipse 60% 70% at 52% 42%, var(--blue-glow) 0%, var(--navy) 45%, var(--navy-deep) 100%);
  }
  .front-scene::after {
    content: ""; position: absolute; left: 0; right: 0; bottom: 0; height: 42%;
    background: linear-gradient(to bottom, rgba(6,8,18,0) 0%, rgba(6,8,18,0.85) 60%, #06080f 100%);
  }
  .front-brand {
    position: absolute; top: 24px; left: 50%; transform: translateX(-50%);
    display: flex; flex-direction: column; align-items: stretch;
    text-align: center;
  }
  .front-brand .brand-name {
    font-size: 30px; font-weight: 700; color: var(--white); line-height: 1.15;
    white-space: nowrap;
  }
  .front-brand .brand-tag {
    margin-top: 3px; padding-top: 3px;
    border-top: 2px solid var(--white);
    font-size: 12px; font-weight: 700; letter-spacing: 5px; text-transform: uppercase;
    color: var(--white); white-space: nowrap;
  }
  .strapline {
    position: absolute; left: 40px; right: 40px; bottom: 40px;
    display: flex; justify-content: space-between;
    list-style: none; font-size: 14px; color: var(--white);
  }
  .strapline li::before { content: "• "; }

  /* Back */
  .card--back { background: var(--white); color: var(--ink); }
  .back-brand {
    position: absolute; top: 30px; left: 30px;
    display: flex; align-items: center; gap: 18px;
  }
  .brand-disc {
    width: 86px; height: 86px; border-radius: 50%;
    background: var(--navy);
    flex: none;
  }
  .back-brand .brand-name {
    font-size: 31px; font-weight: 700; color: var(--brand-blue); line-height: 1.1;
    white-space: nowrap;
  }
  .back-brand .brand-tag {
    margin-top: 4px; padding-top: 3px;
    border-top: 2px solid var(--rule);
    font-size: 12px; font-weight: 700; letter-spacing: 5.2px; text-transform: uppercase;
    color: var(--ink); white-space: nowrap;
  }
  .contacts {
    position: absolute; left: 30px; top: 158px;
    display: grid; grid-template-columns: 62px auto; row-gap: 1px;
    font-size: 13px; color: var(--ink-soft);
  }
  .contacts .person {
    font-weight: 700; color: var(--brand-blue); font-size: 15px;
    align-self: center;
  }
  .contact-line { display: flex; align-items: center; gap: 6px; line-height: 19px; white-space: nowrap; }
  .contact-line svg { width: 14px; height: 14px; fill: var(--brand-blue); flex: none; }
  .span-rows { grid-row: span 2; }
</style>
</head>
<body>
<main class="sheet">

  <section class="card card--front">
    <div class="front-scene" role="img" aria-label="Silhouette of Marsh Priory's towers against a glowing blue night sky"></div>
    <div class="front-brand">
      <div class="brand-name">The Linden Rooms</div>
      <div class="brand-tag">Psychotherapy Practice</div>
    </div>
    <ul class="strapline">
      <li>Professional</li>
      <li>Experienced</li>
      <li>Confidential</li>
    </ul>
  </section>

  <section class="card card--back">
    <div class="back-brand">
      <div class="brand-disc"></div>
      <div>
        <div class="brand-name">The Linden Rooms</div>
        <div class="brand-tag">Psychotherapy Practice</div>
      </div>
    </div>

    <div class="contacts">
      <span class="person span-rows">Maren:</span>
      <span class="contact-line">
        <svg viewBox="0 0 24 24"><path d="M6.6 10.8a15.1 15.1 0 0 0 6.6 6.6l2.2-2.2a1 1 0 0 1 1-.25 11.4 11.4 0 0 0 3.6.57 1 1 0 0 1 1 1V20a1 1 0 0 1-1 1A17 17 0 0 1 3 4a1 1 0 0 1 1-1h3.5a1 1 0 0 1 1 1c0 1.25.2 2.46.57 3.6a1 1 0 0 1-.25 1z"/></svg>
        01632 960412 or 07700 900173
      </span>
      <span class="contact-line">
        <svg viewBox="0 0 24 24"><path d="M2 5h20v14H2zm2 2v.5l8 6 8-6V7z"/></svg>
        info@lindenrooms-therapy.example.co.uk
      </span>
      <span class="person span-rows">Tessa:</span>
      <span class="contact-line">
        <svg viewBox="0 0 24 24"><path d="M6.6 10.8a15.1 15.1 0 0 0 6.6 6.6l2.2-2.2a1 1 0 0 1 1-.25 11.4 11.4 0 0 0 3.6.57 1 1 0 0 1 1 1V20a1 1 0 0 1-1 1A17 17 0 0 1 3 4a1 1 0 0 1 1-1h3.5a1 1 0 0 1 1 1c0 1.25.2 2.46.57 3.6a1 1 0 0 1-.25 1z"/></svg>
        07700 900 358
      </span>
      <span class="contact-line">
        <svg viewBox="0 0 24 24"><path d="M2 5h20v14H2zm2 2v.5l8 6 8-6V7z"/></svg>
        info@tessaholt.example.co.uk
      </span>
      <span></span>
      <span class="contact-line">
        <svg viewBox="0 0 24 24"><path d="M12 2a10 10 0 1 0 0 20 10 10 0 0 0 0-20zm0 2c.9 0 2.1 1.7 2.7 5H9.3C9.9 5.7 11.1 4 12 4zM4.3 11h3a20 20 0 0 0 0 2h-3a8 8 0 0 1 0-2zm5 0h5.4a18 18 0 0 1 0 2H9.3a18 18 0 0 1 0-2zm7.4 0h3a8 8 0 0 1 0 2h-3a20 20 0 0 0 0-2zM9.3 15h5.4c-.6 3.3-1.8 5-2.7 5s-2.1-1.7-2.7-5z"/></svg>
        www.the-linden-rooms.example.co.uk
      </span>
      <span></span>
      <span class="contact-line">
        <svg viewBox="0 0 24 24"><path d="M12 3l10 9h-3v9h-5v-6h-4v6H5v-9H2z"/></svg>
        8 Orchard Row, Marshford, MF3 4QT
      </span>
    </div>
  </section>

</main>
</body>
</html>
```